Website for Dalen Voss

Dalen Voss, an artist, is looking to replace his ClipStream video (Canvases by Dalen Voss) with a new website (dvgallery.example) that functions in much the same way as the ClipStream video, as a slide show, but which makes it much easier to import images and hold them in a library, and to add, subtract, size, rearrange, and choose transitions for a slide show. It should also allow the user to import and manipulate music with a simple interface that allows the user to expand or contract the duration slightly, excerpt and reassemble passages, and make transitions (fade, overlap, etc.) Each slide should be individually editable for screen duration, type of transition, resolution, size, and brightness, however there should be the ability to override the individual settings and create a global setting or apply certain parameters to a subset of slides, perhaps by checking a box or designating subsets by letter group (A,B,C). It would be helpful if the program automatically looked at certain parameters, particularly the brightness of each image, and auto-corrected to make them all the same, if so desired. There should also be a text editor that allows the user to add text to any slide or to create word slides (at an editing level similar to Pixelforge text editing). There would also be the ability to add buttons at any point in the slide show that point to different pages in the site (i.e. "Contact Dalen Voss".), to take email messages and send them to a list of designated email addresses. The site should have the ability to link to other sites.

Industry/Entity Type

Clipstream

Requirements
Must have
• Ease of Use. I'm painter, not a webmaster.
Nice to have
• Elegance

```html
<!DOCTYPE html>
<html lang="en">
<head>
<meta charset="utf-8">
<title>Dalen Voss — Artist</title>
<link rel="stylesheet" href="https://fonts.googleapis.com/css2?family=Tinos:wght@400;700&family=Arimo:wght@400;700&display=swap">
<style>
:root{
  --bg:#1b1b1b;
  --bg-deep:#141414;
  --panel-line:#3a3a3a;
  --yellow:#ffdd00;
  --cream:#fff6c8;
  --heading:#f3e7b4;
  --text:#b9b9b9;
  --muted:#8a8a8a;
  --white:#f4f4f4;
  --nav-bar:#4a4a4a;
  --tab:#4b4b4f;
}
*{box-sizing:border-box;margin:0;padding:0}
html,body{width:1080px;height:1200px;overflow:hidden}
body{
  background:radial-gradient(ellipse at 50% 10%,#2e2e2e 0%,var(--bg) 45%,var(--bg-deep) 100%);
  font-family:"Arimo",Arial,sans-serif;color:var(--text);
  position:relative;
}
.site{position:absolute;left:129px;top:0;width:823px;height:1200px}
a{color:inherit;text-decoration:none}
.serif{font-family:"Tinos","Times New Roman",serif}

/* header */
.header-art{position:absolute;left:470px;top:0;width:353px;height:250px;
  background:radial-gradient(ellipse at 60% 45%,#9a9a9a 0%,#5d5d5d 35%,#2b2b2b 75%,transparent 100%)}
.paint-splash{position:absolute;left:0;top:0;width:110px;height:170px;
  background:linear-gradient(180deg,var(--yellow) 0%,var(--yellow) 60%,rgba(255,221,0,0) 100%)}
.brand{position:absolute;left:100px;top:92px;font-family:"Tinos",serif;font-size:54px;color:var(--yellow);letter-spacing:1px}

/* navigation */
.main-nav{position:absolute;left:0;top:236px;width:694px;height:43px;
  background:linear-gradient(180deg,#5a5a5a,#3c3c3c);border-top:2px solid #111;
  display:flex;align-items:center;padding-left:18px;gap:18px}
.main-nav a{font-family:"Tinos",serif;font-size:14.5px;color:var(--heading)}
.main-nav a.active{color:var(--yellow)}
.video-tab{position:absolute;left:643px;top:253px;width:180px;height:51px;
  background:linear-gradient(180deg,#4e4e4e,#353535);display:flex;align-items:center;justify-content:center;
  font-family:"Tinos",serif;font-size:26px;color:var(--yellow)}

/* left column */
.sidebar{position:absolute;left:0;top:322px;width:154px}
.search{display:flex;gap:8px}
.search-select{width:120px;height:22px;border:1px solid var(--panel-line);background:#1e1e1e;
  font-size:10px;color:var(--muted);display:flex;align-items:center;justify-content:space-between;padding:0 8px}
.search-select svg{width:9px;height:6px}
.btn-go{width:25px;height:22px;background:var(--yellow);color:#222;font-size:14px;display:flex;align-items:center;justify-content:center;font-weight:700}
.side-box{margin-top:18px;border:1px solid var(--panel-line)}
.side-group{padding:14px 16px 12px;border-bottom:1px solid var(--panel-line)}
.side-group:last-child{border-bottom:none}
.side-title{font-family:"Tinos",serif;font-size:13.5px;color:var(--heading);margin-bottom:5px}
.link-list{list-style:none}
.link-list li{font-size:10.5px;line-height:17.3px;color:var(--text);padding-left:14px;position:relative}
.link-list li::before{content:"";position:absolute;left:1px;top:5px;border-left:5px solid #bbb;border-top:4px solid transparent;border-bottom:4px solid transparent}
.follow{margin-top:18px}
.follow .side-title{margin-bottom:8px}
.social{display:flex;gap:8px}
.social span{width:30px;height:28px;border-radius:4px;background:linear-gradient(180deg,#7c7c7c,#3d3d3d);
  font-size:6.5px;color:var(--white);display:flex;align-items:center;justify-content:center;text-align:center}

/* center column */
.feature{position:absolute;left:171px;width:480px;background:var(--cream);padding:8px}
.feature div{width:100%;height:100%}
.feature-1{top:322px;height:223px}
.feature-1 div{background:linear-gradient(180deg,#d9d0c0 0%,#a68d6a 35%,#7a5a2f 65%,#4b3720 100%)}
.caption{position:absolute;left:171px;top:561px;font-family:"Tinos",serif;font-size:11.5px;color:var(--white)}
.feature-2{top:579px;height:137px}
.feature-2 div{background:linear-gradient(180deg,#a9c2d6 0%,#6f8aa0 40%,#d8dde0 80%,#8d9aa5 100%)}
.tabs{position:absolute;left:171px;top:734px;display:flex;gap:2px}
.tab{height:26px;background:var(--tab);color:var(--white);font-family:"Tinos",serif;font-size:15px;padding:0 9px;display:flex;align-items:center;gap:4px}
.tab b{font-family:"Arimo",sans-serif;font-size:14px}
.tab.active{height:34px;background:var(--yellow);color:#222;font-size:18px}
.tab.active b{font-size:18px}
.thumbs{position:absolute;left:171px;top:776px;width:480px;display:grid;grid-template-columns:repeat(3,156px);gap:6px}
.thumb{height:103px;background:var(--cream);padding:5px}
.thumb div{width:100%;height:100%}

/* right column */
.aside{position:absolute;left:669px;top:322px;width:154px;height:666px;border:1px solid var(--panel-line)}
.aside-group{padding:16px 16px 14px;border-bottom:1px solid var(--panel-line)}
.aside-group:last-child{border-bottom:none}
.aside-date{font-family:"Tinos",serif;font-size:11.5px;color:var(--text)}
.auction-art{margin-top:8px;width:120px;height:103px;background:var(--cream);padding:5px}
.auction-art div{width:100%;height:100%;background:linear-gradient(135deg,#2bb39a,#1b6e60 60%,#c8d8c0)}
.more{display:block;text-align:right;font-family:"Tinos",serif;font-size:11px;color:var(--white);text-decoration:underline;margin-top:4px}
.article{margin-top:8px}
.article-date{font-size:10.5px;color:var(--heading)}
.article p{font-size:10px;line-height:15.5px;color:var(--muted)}
.field{height:22px;border:1px solid var(--panel-line);margin-top:9px;font-size:10px;color:var(--muted);display:flex;align-items:center;padding-left:11px}
.btn-submit{display:block;margin:10px 0 0 auto;width:64px;height:22px;background:var(--yellow);color:#222;font-size:15px;text-align:center;line-height:22px}

/* footer */
.footer{position:absolute;left:0;top:1014px;width:823px;border-top:1px solid #333}
.footer-nav{margin-top:30px;font-size:11.5px;color:var(--muted);word-spacing:2px}
.footer-nav .active{color:var(--yellow)}
.copyright{margin-top:13px;font-size:11.5px;color:var(--muted)}
.copyright .owner{color:var(--yellow)}
</style>
</head>
<body>
<div class="site">
  <header>
    <div class="header-art" role="img" aria-label="Painted portrait artwork in grey tones"></div>
    <div class="paint-splash" role="img" aria-label="Yellow paint splash"></div>
    <div class="brand">Dalen Voss</div>
  </header>

  <nav class="main-nav">
    <a class="active" href="#">Home</a><a href="#">Gallery</a><a href="#">Conservation</a><a href="#">Consultation</a><a href="#">Profile</a><a href="#">Paintings</a><a href="#">Cost</a><a href="#">Bibliography</a><a href="#">e-mail</a>
  </nav>
  <div class="video-tab">Latest Video</div>

  <aside class="sidebar">
    <div class="search">
      <div class="search-select">search by artist
        <svg viewBox="0 0 9 6"><path d="M0 0h9L4.5 6z" fill="#aaa"/></svg>
      </div>
      <div class="btn-go">Go</div>
    </div>
    <div class="side-box">
      <div class="side-group">
        <h3 class="side-title">Quick Links</h3>
        <ul class="link-list"><li>Browse &amp; Buy</li><li>Auctions</li><li>Exibitons</li><li>Art Guide</li><li>Art Directory</li></ul>
      </div>
      <div class="side-group">
        <h3 class="side-title">Upcoming Shows</h3>
        <ul class="link-list"><li>Marek Tolliver</li></ul>
      </div>
      <div class="side-group">
        <h3 class="side-title">Past Shows</h3>
        <ul class="link-list"><li>Spring Thaw, 2010</li><li>Sandy Pond, 2009</li><li>Flying Eagle, 1963</li><li>Secret Place, 2010</li><li>Crossroads, 2009</li><li>Paradise, 2009</li><li>Peaceful Cove, 2009</li></ul>
      </div>
    </div>
    <div class="follow">
      <h3 class="side-title">Follow Us On</h3>
      <div class="social"><span>Friendbook</span><span>Chirper</span><span>ClipStream</span><span>Feed</span></div>
    </div>
  </aside>

  <main>
    <div class="feature feature-1"><div role="img" aria-label="Autumn landscape painting with lake and mountains"></div></div>
    <p class="caption">Lorem ipsum dolor sit amet, consectetur adipiscing elit. Nulla vulputate purus quis dapibus.</p>
    <div class="feature feature-2"><div role="img" aria-label="Winter street painting with traffic lights and houses"></div></div>
    <div class="tabs">
      <div class="tab active"><b>01.</b> Artist</div>
      <div class="tab"><b>02.</b> Modern</div>
      <div class="tab"><b>03.</b> Contemporary</div>
      <div class="tab"><b>03.</b> Sculpture</div>
    </div>
    <div class="thumbs">
      <div class="thumb"><div role="img" aria-label="Snowy hillside painting" style="background:linear-gradient(180deg,#9fb0c0,#dfe3e6 50%,#8a6a45)"></div></div>
      <div class="thumb"><div role="img" aria-label="Stream under trees painting" style="background:linear-gradient(180deg,#cfd6dc,#2e4a24 40%,#6a7f8a 75%,#3a3a24)"></div></div>
      <div class="thumb"><div role="img" aria-label="Spring farmhouse painting" style="background:linear-gradient(180deg,#d5d9d0,#b89a6a 55%,#8f6e4a)"></div></div>
      <div class="thumb"><div role="img" aria-label="City street crossing painting" style="background:linear-gradient(180deg,#7a4a3a,#c49a6a 50%,#9a3a2a)"></div></div>
      <div class="thumb"><div role="img" aria-label="Coastal seascape painting" style="background:linear-gradient(180deg,#a48aa0,#6a5e6e 50%,#343a3e)"></div></div>
      <div class="thumb"><div role="img" aria-label="Still life painting of pears" style="background:linear-gradient(135deg,#1c2018,#7a8a2a 50%,#2a2418)"></div></div>
    </div>
  </main>

  <aside class="aside">
    <div class="aside-group">
      <h3 class="side-title" style="margin-bottom:1px">Summer Auction</h3>
      <div class="aside-date">July 15-16 , 2013</div>
      <div class="auction-art"><div role="img" aria-label="Colourful expressive painting for auction"></div></div>
      <a class="more" href="#">Aution Results</a>
    </div>
    <div class="aside-group">
      <h3 class="side-title">Published Articles</h3>
      <div class="article"><div class="article-date">04 July 2013</div><p>Lorem ipsum dolor sit amet, conse ctetur adip iscing elit.</p><a class="more" href="#">read more</a></div>
      <div class="article"><div class="article-date">04 July 2013</div><p>Lorem ipsum dolor sit amet, conse ctetu.</p><a class="more" href="#" style="margin-top:-4px">read more</a></div>
      <div class="article"><div class="article-date">04 July 2013</div><p>Lorem ipsum dolor sit amet, conse ctetur adip iscing elit.</p><a class="more" href="#">read more</a></div>
    </div>
    <div class="aside-group">
      <h3 class="side-title">Subscribe to Our Newsletter</h3>
      <div class="field">Your Name</div>
      <div class="field">Your Email Address</div>
      <span class="btn-submit">Submit</span>
    </div>
  </aside>

  <footer class="footer">
    <div class="footer-nav"><span class="active">Home</span> &nbsp;| &nbsp;Gallery &nbsp;| &nbsp;Conservation &nbsp;| &nbsp;Consultation &nbsp;| &nbsp;Profile &nbsp;| &nbsp;Paintings &nbsp;| &nbsp;Cost &nbsp;| &nbsp;Bibliography &nbsp; | &nbsp;Articles &nbsp;| &nbsp;e-mail</div>
    <div class="copyright">Copyright © 2013 &nbsp;<span class="owner">Marek Tolliver</span>. All rights reserved &nbsp;| &nbsp;Terms &amp; Conditions</div>
  </footer>
</div>
</body>
</html>
```